Business Card Design for Varnel

I've already got the logo, but I'd like to see some interesting designs.

I don't want anything to complex. I like it simple,yet innovative, like the logo.

My business is System Administration for small to medium size businesses, so that will be my main target audience.
Updates

hey all, the png has been uploaded.

Hey all,

If you are submitting the back side of the card, I'd like the top bit of the card to be Varnel Solutions and the logo, the bottom of the card the website, with a white background.

The middle I'd like to leave blank for a quote that will be printed on each card.

Thanks!

Doug

Industry/Entity Type

Business

```html
<!DOCTYPE html>
<html lang="en">
<head>
<meta charset="utf-8">
<title>Varnel Solutions — Business Cards</title>
<link href="https://fonts.googleapis.com/css2?family=Open+Sans:wght@400;600;700&display=swap" rel="stylesheet">
<style>
  :root {
    --page-bg: #ecebe8;
    --card-bg: #ffffff;
    --brand-blue: #2a6fb0;
    --band-light: #29a3de;
    --band-dark: #2a6fb0;
    --text-grey: #4a4a4a;
    --rule-grey: #d2d2d2;
  }
  * { box-sizing: border-box; margin: 0; padding: 0; }
  html, body {
    width: 1200px; height: 758px; overflow: hidden;
    background: var(--page-bg);
    font-family: "Open Sans", Arial, sans-serif;
  }
  .canvas {
    position: relative; width: 1200px; height: 758px;
    display: flex; align-items: center; justify-content: center; gap: 50px;
  }
  .card {
    position: relative; width: 540px; height: 310px;
    background: var(--card-bg); border-radius: 26px; overflow: hidden;
    box-shadow: 0 6px 18px rgba(0,0,0,.18);
  }

  /* Front */
  .card-front .brand {
    position: absolute; left: 36px; top: 92px; width: 246px;
    display: flex; align-items: center; gap: 10px;
  }
  .brand-dot {
    width: 50px; height: 50px; border-radius: 50%; background: var(--brand-blue);
    flex: none;
  }
  .brand-name {
    font-weight: 700; color: var(--brand-blue); font-size: 20px; line-height: 1;
    white-space: nowrap;
  }
  .card-front .divider {
    position: absolute; left: 296px; top: 40px; width: 1px; height: 140px;
    background: linear-gradient(var(--rule-grey), rgba(210,210,210,0));
  }
  .contact {
    position: absolute; left: 316px; top: 36px; color: var(--text-grey);
  }
  .contact .person-name {
    font-weight: 700; color: var(--brand-blue); font-size: 18px; line-height: 1.2;
  }
  .contact .person-title { font-size: 14px; margin: 4px 0 8px; }
  .contact ul { list-style: none; font-size: 12.5px; line-height: 18px; }
  .contact li { display: flex; align-items: center; gap: 7px; }
  .contact svg { width: 10px; height: 10px; fill: var(--text-grey); flex: none; }

  .band {
    position: absolute; left: 0; right: 0; top: 196px; height: 34px;
    background: linear-gradient(90deg, var(--band-dark), var(--band-light));
  }
  .band-dot {
    position: absolute; right: 54px; top: 186px; width: 54px; height: 54px;
    border-radius: 50%; background: var(--card-bg);
    display: flex; align-items: center; justify-content: center;
  }
  .band-dot span { width: 40px; height: 40px; border-radius: 50%; background: var(--brand-blue); }
  .address {
    position: absolute; left: 0; right: 0; top: 258px; text-align: center;
    font-size: 13px; letter-spacing: 1.2px; color: var(--text-grey);
  }

  /* Back */
  .card-back .brand {
    position: absolute; left: 0; right: 0; top: 82px;
    display: flex; align-items: center; justify-content: center; gap: 20px;
  }
  .card-back .brand-dot { width: 100px; height: 100px; }
  .card-back .brand-name { font-size: 38px; }
  .website {
    position: absolute; left: 0; right: 0; top: 232px; text-align: center;
    font-size: 22px; letter-spacing: 3px; color: var(--text-grey);
  }
</style>
</head>
<body>
<main class="canvas">
  <section class="card card-front" aria-label="Card front">
    <div class="brand">
      <span class="brand-dot"></span>
      <span class="brand-name">Varnel Solutions</span>
    </div>
    <div class="divider"></div>
    <div class="contact">
      <p class="person-name">Your Name</p>
      <p class="person-title">Title</p>
      <ul>
        <li><svg viewBox="0 0 10 10"><path d="M2 0.5 3.6 2.6 2.7 3.6Q3.8 6 6.4 7.3L7.4 6.4 9.5 8 8.4 9.5Q3 9 0.5 1.6Z"/></svg>123-456-789</li>
        <li><svg viewBox="0 0 10 10"><rect x="1" y="4" width="8" height="6" rx="1"/><rect x="0" y="1" width="10" height="3" rx="1.5"/></svg>123-456-789</li>
        <li><svg viewBox="0 0 10 10"><path d="M0 2h10v6H0z M0 2l5 3.5L10 2" stroke="#fff" stroke-width=".8"/></svg>info@varnelmail.com</li>
        <li><svg viewBox="0 0 10 10"><circle cx="5" cy="5" r="4.5"/><path d="M0.5 5h9M5 .5v9" stroke="#fff" stroke-width=".7"/></svg>www.website.com</li>
      </ul>
    </div>
    <div class="band"></div>
    <div class="band-dot"><span></span></div>
    <p class="address">00, Complex name, City, State 0032</p>
  </section>

  <section class="card card-back" aria-label="Card back">
    <div class="brand">
      <span class="brand-dot"></span>
      <span class="brand-name">Varnel Solutions</span>
    </div>
    <p class="website">www.website.com</p>
  </section>
</main>
</body>
</html>
```